Knife Group for Tarn, Fenn, & Orlo Knives

I have a new KL group set-up and I only have 40 members. I want to grow it by making sure I have it set-up correctly and optimize it and improve the looks. I want members to feel comfortable to post ideas, comments, pictures, etc. I have it set-up as a club that is closed until a person joins. Is it best to be closed or public for what I am doing? I sell knives on zuMart under seller ID mqvossel. I also want my KL group to feed traffic to my zuMart store. I also have a stand alone web store using strelka @ http://www.strelka.example/stores/mqvossel4837/ This will soon be updated to URL, vosselsblades.example Look at other KL knife groups to make my group better over time.

Target Market(s)

Knife collectors of Tarn, Fenn, and Orlo knives. Also any person interested in People wanting to learn more about knife collecting and they can see and post pictures of mint rare knives.

Font styles to use
Sans Serif

Colors
0255a3
ec1f27

Requirements
Must have
• Insure I have set-up my KL group correctly to target the most people. It was set-up from my page. Is there a way to only have a group, but not the page? Improve the looks of the landing page and add any unique features. I also want a landing page that stands out from others. I want it easy as possible for people to join. I am unable to boost post even if I pay KL as they send emails that boost not arrived because I am selling knives which is not true.
Nice to have
• Is it possible to have the language be for the country the person is seeing it in or does KL do that automatically? My 2 favorite colors are blue and red. I want to site to look excellent with the best colors. I am easy to work with. I want the designer to think and use their ideas along with what I want to improve what I have started.

```html
<!DOCTYPE html>
<html lang="en">
<head>
<meta charset="utf-8">
<title>Vossel's Collectible Cutlery – Welcome Banner</title>
<link rel="stylesheet" href="https://fonts.googleapis.com/css2?family=Montserrat:wght@500;700;800&display=swap">
<style>
  :root {
    --brand-blue: #0255a3;
    --brand-red: #ec1f27;
    --paper-white: #ffffff;
    --name-slate: #4a5563;
    --wood-dark: #3b2417;
    --wood-mid: #6b4630;
    --wood-light: #8a6245;
    --blade-gold: #c9b27a;
    --shell-green: #6f8a6a;
    --shell-pearl: #d9d3bf;
  }
  html, body {
    margin: 0;
    padding: 0;
    width: 1200px;
    height: 670px;
    overflow: hidden;
    background: var(--paper-white);
  }
  .banner {
    position: relative;
    width: 1200px;
    height: 670px;
    overflow: hidden;
    font-family: "Montserrat", Arial, sans-serif;
  }
  .banner__shapes {
    position: absolute;
    inset: 0;
    width: 1200px;
    height: 670px;
    display: block;
  }
  .welcome {
    position: absolute;
    left: 34px;
    top: 132px;
    width: 330px;
  }
  .welcome__greeting {
    margin: 0 0 8px 20px;
    font-size: 25px;
    font-weight: 500;
    color: var(--brand-blue);
    letter-spacing: 0.2px;
  }
  .welcome__name {
    margin: 0;
    padding-left: 20px;
    font-size: 44px;
    font-weight: 800;
    line-height: 1;
    color: var(--name-slate);
    letter-spacing: -0.5px;
  }
  .welcome__name span {
    display: block;
    font-size: 21px;
    margin-top: 8px;
    letter-spacing: 0.3px;
  }
  .offer {
    position: absolute;
    left: 58px;
    top: 398px;
    margin: 0;
    color: var(--paper-white);
    font-size: 29px;
    font-weight: 500;
    line-height: 38px;
  }
  .offer strong {
    display: block;
    font-size: 32px;
    font-weight: 700;
    line-height: 42px;
  }
</style>
</head>
<body>
  <main class="banner">
    <svg class="banner__shapes" viewBox="0 0 828 462" preserveAspectRatio="none" aria-hidden="false">
      <defs>
        <linearGradient id="woodTone" x1="0" y1="0" x2="1" y2="1">
          <stop offset="0" stop-color="var(--wood-light)"/>
          <stop offset="0.5" stop-color="var(--wood-mid)"/>
          <stop offset="1" stop-color="var(--wood-dark)"/>
        </linearGradient>
        <linearGradient id="knifeTone" x1="0" y1="0" x2="1" y2="1">
          <stop offset="0" stop-color="var(--blade-gold)"/>
          <stop offset="0.55" stop-color="var(--shell-pearl)"/>
          <stop offset="1" stop-color="var(--shell-green)"/>
        </linearGradient>
      </defs>
      <rect class="wood-surface" x="0" y="0" width="828" height="462" fill="url(#woodTone)" role="img" aria-label="Dark walnut wood table surface"/>
      <polygon class="band-red" points="0,0 410,0 700,175 330,462 0,462" fill="var(--brand-red)"/>
      <polygon class="wedge-white" points="0,0 122,0 512,155 0,268" fill="var(--paper-white)"/>
      <polygon class="band-blue" points="545,250 828,88 828,335 690,330" fill="var(--brand-blue)"/>
      <polygon class="knife-display" points="410,175 450,165 560,170 700,105 740,100 828,240 828,462 470,462 420,300" fill="url(#knifeTone)" opacity="0.92" role="img" aria-label="Three collectible knives with gold blades and abalone and stag handles"/>
    </svg>

    <header class="welcome">
      <p class="welcome__greeting">Thanks for visiting</p>
      <h1 class="welcome__name">Vossel's<span>Collectible Cutlery</span></h1>
    </header>

    <p class="offer">
      <strong>We offer outstanding knives,</strong>
      straight razors, and unique items<br>
      and exceptional customer service
    </p>
  </main>
</body>
</html>
```